BRELTONAllies.co.uk - Mental Health Clinic for Child and Adolescents

Updated 29/01/2018***
I am not sure you guys are getting the idea regards to the opening page / homescreen layout. Can you look at the new images I have uploaded (page 5, 6 and 7) These are some of the layouts I like but to incorporate my chosen images, with the BRELTON ALLIES commissioner, buttons and a sliding header bar.
I have written a strong brief, I am looking for a website, preferably wordpress as i know they are easy to maintain. I am looking for a one page site, with the top / opening page being full screen image with drop down categories. I have made a rough design, see full brief in word doc attached, there is some freedom to play around with the design aspect but it will need to relay all the content provided. I like a minimal feel. I have also attached some images that may be useful, but will need a new logo for BRELTON Allies. I have attached some logo idea's, it is up to you decide whether you want to use them.
I would prefer the homepage as full screen image, and the categories offered as a drop down or over the main image.
I have also attached linked to some competitors websites:
https://www.vorrendale-group.co.uk/
http://www.qmvd.org.uk/
Industry/Entity Type
Clinic
Number of Pages Required
1 page
Font styles to use
Look and feel
Each slider illustrates characteristics of the customer's brand and the style your logo design should communicate.

```html
<!DOCTYPE html>
<html lang="en">
<head>
<meta charset="utf-8">
<title>BRELTON Allies – Where Young Minds Matter</title>
<link rel="stylesheet" href="https://fonts.googleapis.com/css2?family=Open+Sans:wght@400;600&family=Poppins:wght@400&family=Arimo:wght@400&display=swap">
<style>
  :root {
    --teal: #12957d;
    --purple: #6a1b72;
    --white: #ffffff;
    --ink: #111111;
    --line: #dcdcdc;
    --photo-a: #9fd3c8;
    --photo-b: #cfeee7;
    --photo-c: #7fbfb1;
    --footer-accent: #2ad0b0;
  }
  * { margin: 0; padding: 0; box-sizing: border-box; }
  html, body { width: 1200px; height: 600px; overflow: hidden; }
  body { font-family: "Open Sans", Arial, sans-serif; background: var(--white); }

  .home { position: relative; width: 1200px; height: 600px; overflow: hidden; }

  .hero-photo {
    position: absolute; inset: 0 0 0 66px;
    background:
      radial-gradient(ellipse at 85% 25%, var(--photo-b) 0%, transparent 55%),
      linear-gradient(100deg, var(--photo-c) 0%, var(--photo-a) 45%, var(--photo-b) 100%);
  }

  .brand {
    position: absolute; left: 0; top: 0; width: 155px; height: 86px;
    background: var(--white);
    display: flex; flex-direction: column; justify-content: center; padding-left: 10px;
  }
  .brand-name { font-size: 17px; font-weight: 600; color: var(--purple); line-height: 1.2; }
  .brand-tagline { font-size: 9.5px; font-weight: 600; color: var(--purple); margin-top: 6px; }

  .menu-toggle {
    position: absolute; left: 0; top: 86px; width: 155px; height: 87px;
    background: var(--teal); color: var(--white);
    display: flex; align-items: center;
  }
  .menu-toggle svg { margin-left: 17px; }
  .menu-toggle span { margin-left: 42px; font-size: 14px; font-weight: 400; }

  .side-nav {
    position: absolute; left: 0; top: 173px; width: 66px; height: 427px;
    background: var(--white); list-style: none;
  }
  .side-nav li {
    height: 81px; border-bottom: 1px solid var(--line);
    display: flex; align-items: center; justify-content: center;
  }

  .hero-content {
    position: absolute; left: 380px; top: 240px; width: 456px; text-align: center;
  }
  .hero-title {
    font-family: "Arimo", Arial, sans-serif; font-weight: 400;
    font-size: 38px; line-height: 46px; color: var(--ink); letter-spacing: 0.4px;
  }
  .hero-text {
    width: 360px; margin: 12px auto 0;
    font-size: 13px; line-height: 20px; color: #222;
  }

  .cta-row { margin-top: 24px; display: flex; justify-content: center; gap: 10px; }
  .cta {
    position: relative; display: block; height: 32px; width: 136px;
    border-radius: 16px; overflow: hidden; text-decoration: none;
    background: var(--white); color: var(--white); font-size: 12.5px;
  }
  .cta-label {
    position: absolute; left: 0; top: 0; bottom: 0; width: 110px;
    display: flex; align-items: center; justify-content: center;
    padding-right: 12px; white-space: nowrap;
    clip-path: polygon(0 0, 100% 0, 82% 100%, 0 100%);
  }
  .cta-arrow {
    position: absolute; right: 0; top: 0; bottom: 0; width: 34px;
    display: flex; align-items: center; justify-content: center;
  }
  .cta--parents .cta-label { background: var(--teal); }
  .cta--commissioners .cta-label { background: var(--purple); padding-left: 2px; padding-right: 14px; }

  .site-footer {
    position: absolute; left: 66px; right: 0; bottom: 17px; text-align: center;
    font-family: "Poppins", Arial, sans-serif; font-size: 10px; color: var(--white);
  }
  .site-footer a { color: var(--footer-accent); text-decoration: none; }
</style>
</head>
<body>
<main class="home">
  <div class="hero-photo" role="img" aria-label="Photograph of a therapist talking with a teenage girl in a bright room, tinted teal"></div>

  <div class="brand">
    <span class="brand-name">BRELTON Allies</span>
    <span class="brand-tagline">Where Young Minds Matter</span>
  </div>

  <div class="menu-toggle">
    <svg width="28" height="20" viewBox="0 0 28 20" aria-hidden="true">
      <g stroke="#fff" stroke-width="2.2"><line x1="0" y1="2" x2="28" y2="2"/><line x1="0" y1="10" x2="28" y2="10"/><line x1="0" y1="18" x2="28" y2="18"/></g>
    </svg>
    <span>MENU</span>
  </div>

  <ul class="side-nav">
    <li><svg width="28" height="30" viewBox="0 0 28 30" fill="none" stroke="#222" stroke-width="1.3" aria-hidden="true"><rect x="2" y="4" width="20" height="24"/><path d="M5 1v5M9 1v5M13 1v5M17 1v5M6 12h10M6 17h7M6 22h6"/><path d="M26 10 16 24l-2 3 3-2 10-14z"/></svg></li>
    <li><svg width="34" height="28" viewBox="0 0 34 28" fill="none" stroke="#222" stroke-width="1.3" aria-hidden="true"><circle cx="17" cy="8" r="5"/><circle cx="7" cy="12" r="4"/><circle cx="27" cy="12" r="4"/><path d="M9 27c0-6 4-10 8-10s8 4 8 10M1 27c0-5 3-8 6-8M33 27c0-5-3-8-6-8"/></svg></li>
    <li><svg width="30" height="30" viewBox="0 0 30 30" fill="none" stroke="#222" stroke-width="1.3" aria-hidden="true"><path d="M4 22 22 4l4 4L8 26z"/><path d="M10 16l2 2M13 13l2 2M16 10l2 2"/><path d="M4 4l4 0 18 18-2 4-4 0L2 8z"/></svg></li>
    <li><svg width="26" height="26" viewBox="0 0 26 26" fill="none" stroke="#222" stroke-width="1.3" aria-hidden="true"><path d="M6 2l4 6-3 3c1 3 5 7 8 8l3-3 6 4-3 4C12 24 2 14 2 5z"/></svg></li>
    <li><svg width="30" height="30" viewBox="0 0 30 30" fill="none" stroke="#222" stroke-width="1.3" aria-hidden="true"><rect x="2" y="2" width="26" height="26"/><path d="M2 10h26M2 19h26M6 6h14M6 14h8M18 14h6M6 23h10"/></svg></li>
  </ul>

  <section class="hero-content">
    <h1 class="hero-title">EDUCATION TEMPLTE</h1>
    <p class="hero-text">BRELTON Allies was formed with a vision to provide the very best CAMHS assessments, therapy and aftercare.</p>
    <div class="cta-row">
      <a class="cta cta--parents" href="#parents">
        <span class="cta-label">Parewts</span>
        <span class="cta-arrow"><svg width="18" height="12" viewBox="0 0 18 12" fill="none" stroke="#12957d" stroke-width="1.5"><path d="M0 6h16M11 1l5 5-5 5"/></svg></span>
      </a>
      <a class="cta cta--commissioners" href="#commissioners">
        <span class="cta-label">Commissioners</span>
        <span class="cta-arrow"><svg width="18" height="12" viewBox="0 0 18 12" fill="none" stroke="#6a1b72" stroke-width="1.5"><path d="M0 6h16M11 1l5 5-5 5"/></svg></span>
      </a>
    </div>
  </section>

  <footer class="site-footer">© 2018 All Rights Reserved.<a href="#">breltonallies.com</a></footer>
</main>
</body>
</html>
```